Logo & Stationery Design

We are a new company based in Sydney, Australia called Brivana Fresh Pantry. We import and distribute top quality olive oil to restaurants and deli's, etc.
We need a logo design, business cards and letterheads for our company.
For the logo we would like to see designs that include an olive branch (olives and leaves) and that include the colours green and purple. Please see examples attached.
We would like a health, wellness and nature feel in the design.
For the business cards and letterheads we would like to add an illustration with a tag line. We would like to see something along the lines of oil dripping from an olive into a champagne glass with the tag line "top drop"

```html
<!DOCTYPE html>
<html lang="en">
<head>
<meta charset="utf-8">
<title>Brivana Fresh Pantry – Business Card</title>
<link rel="stylesheet" href="https://fonts.googleapis.com/css2?family=Arimo:wght@400;700&family=Tinos&display=swap">
<style>
  :root {
    --backdrop: #3a3a3c;
    --card-dark: #2c2829;
    --card-light: #f4f4f4;
    --leaf-green: #7ccd3f;
    --olive-purple: #8a4fc0;
  }
  * { margin: 0; padding: 0; box-sizing: border-box; }
  html, body {
    width: 1200px;
    height: 900px;
    overflow: hidden;
    background: var(--backdrop);
    font-family: "Arimo", Arial, sans-serif;
  }
  .stage {
    position: relative;
    width: 1200px;
    height: 900px;
  }
  .card {
    position: absolute;
    width: 580px;
    height: 330px;
    border-radius: 2px;
    box-shadow: 0 12px 34px rgba(0,0,0,0.5);
  }

  /* Contact side */
  .card-back {
    left: 60px;
    top: 80px;
    background: linear-gradient(135deg, #ffffff 0%, var(--card-light) 55%, #e4e4e4 100%);
  }
  .contact {
    position: absolute;
    left: 50px;
    top: 58px;
    color: var(--leaf-green);
  }
  .contact-name {
    font-size: 24px;
    line-height: 1;
  }
  .contact-position {
    font-size: 12px;
    font-weight: 700;
    margin: 5px 0 0 2px;
  }
  .contact-details {
    list-style: none;
    margin-top: 26px;
    font-size: 13px;
    line-height: 18px;
  }
  .divider {
    position: absolute;
    left: 300px;
    top: 120px;
    width: 2px;
    height: 170px;
    background: var(--leaf-green);
  }
  .brand {
    display: flex;
    align-items: center;
    font-family: "Tinos", "Times New Roman", serif;
    font-weight: 400;
    color: var(--leaf-green);
  }
  .brand-mark {
    border-radius: 50%;
    background: var(--olive-purple);
    flex: none;
  }
  .brand-name { line-height: 1.05; }

  .card-back .brand {
    position: absolute;
    left: 322px;
    top: 178px;
    gap: 14px;
  }
  .card-back .brand-mark { width: 40px; height: 40px; }
  .card-back .brand-name { font-size: 30px; }

  /* Brand side */
  .card-front {
    left: 560px;
    top: 450px;
    background: linear-gradient(160deg, #332e2f 0%, var(--card-dark) 60%, #242021 100%);
    display: flex;
    align-items: center;
    justify-content: center;
  }
  .card-front .brand { gap: 26px; }
  .card-front .brand-mark { width: 86px; height: 86px; }
  .card-front .brand-name { font-size: 56px; }
</style>
</head>
<body>
  <main class="stage">
    <section class="card card-back" aria-label="Business card, contact side">
      <div class="contact">
        <p class="contact-name">Your Name</p>
        <p class="contact-position">Position</p>
        <ul class="contact-details">
          <li>Address: xxxxxxxxxxxxxxxxx</li>
          <li>Phone: xxxxxxxxxxxxxxxxxx</li>
          <li>Fax:xxxxxxxxxxxxxxxxxxxx</li>
          <li>Email: xxxxxxxxxxxxxxxxxx</li>
        </ul>
      </div>
      <div class="divider"></div>
      <div class="brand">
        <span class="brand-mark"></span>
        <p class="brand-name">Brivana<br>Fresh Pantry</p>
      </div>
    </section>

    <section class="card card-front" aria-label="Business card, brand side">
      <div class="brand">
        <span class="brand-mark"></span>
        <p class="brand-name">Brivana<br>Fresh Pantry</p>
      </div>
    </section>
  </main>
</body>
</html>
```